SkyvoraQ Business Cards and Stationary Design

Need a design for our business cards and stationary. I want to carry on the theme of the logo. I want the business cards to have a design on the back. I would like the business cards and the stationary to carry the same theme, design scheme, and branding

Target Market(s)

Airlines and Maintenance Facilities

Industry/Entity Type

Aviation

Contact Information for Business Card

Name
Position Title
Address: 4827 Tollbeck Lane, Larkhaven, Calvera, 34951
Office Number
Mobile Number
Email
Website

Font styles to use
Serif
Sans Serif

Colors

Designer to choose colors to be used in the design.

```html
<!DOCTYPE html>
<html lang="en">
<head>
<meta charset="utf-8">
<title>SkyvoraQ Business Card</title>
<link rel="stylesheet" href="https://fonts.googleapis.com/css2?family=Quicksand:wght@400;500;700&display=swap">
<style>
  :root {
    --page: #eceef1;
    --paper: #ffffff;
    --navy: #1d2c57;
    --deep-blue: #0f4e8c;
    --sky: #2ba1db;
    --sky-light: #3aa8de;
    --ink: #4a4a4a;
    --ink-soft: #5f5f5f;
    --rule: #b9b9b9;
  }
  * { margin: 0; padding: 0; box-sizing: border-box; }
  html, body { width: 1200px; height: 960px; overflow: hidden; }
  body {
    background: var(--page);
    font-family: "Quicksand", sans-serif;
    position: relative;
  }
  .card {
    position: absolute;
    left: 250px;
    width: 700px;
    height: 400px;
    border-radius: 4px;
    overflow: hidden;
    box-shadow: 0 6px 18px rgba(0,0,0,0.18);
  }
  /* Back */
  .card-back {
    top: 50px;
    background: linear-gradient(160deg, var(--sky-light) 0%, #2a6fa8 50%, var(--navy) 100%);
    color: #fff;
  }
  .card-back .brand {
    position: absolute;
    left: 0; right: 0; top: 150px;
    display: flex; flex-direction: column; align-items: center; gap: 18px;
  }
  .brand-dot {
    width: 62px; height: 62px; border-radius: 50%;
    border: 6px solid currentColor;
  }
  .brand-name {
    font-weight: 700;
    font-size: 46px;
    letter-spacing: 12px;
    text-transform: uppercase;
  }
  .card-back .web {
    position: absolute; right: 40px; bottom: 30px;
    font-size: 17px; font-weight: 500; letter-spacing: 1px;
  }
  /* Front */
  .card-front {
    top: 510px;
    background: var(--paper);
  }
  .card-front .brand {
    position: absolute;
    left: 40px; width: 300px; top: 95px;
    display: flex; flex-direction: column; align-items: center; gap: 14px;
    color: var(--navy);
  }
  .card-front .brand-dot { width: 72px; height: 72px; border-color: var(--deep-blue); }
  .card-front .brand-name { font-size: 34px; letter-spacing: 8px; }
  .divider {
    position: absolute; left: 370px; top: 70px;
    width: 1px; height: 200px; background: var(--rule);
  }
  .contact {
    position: absolute; left: 400px; top: 62px; color: var(--ink-soft);
  }
  .person { font-size: 28px; font-weight: 700; color: var(--ink); }
  .person .surname { text-transform: uppercase; }
  .role { font-size: 17px; margin-top: 0; }
  .address { font-size: 17px; line-height: 1.35; margin-top: 16px; }
  .lines { list-style: none; margin-top: 14px; font-size: 18px; }
  .lines li { display: flex; align-items: center; gap: 12px; line-height: 1.5; }
  .lines svg { width: 16px; height: 16px; fill: none; stroke: var(--sky); stroke-width: 1.6; }
  .band {
    position: absolute; left: 0; right: 0; bottom: 0; height: 80px;
    background: linear-gradient(90deg, var(--navy) 0%, var(--deep-blue) 70%, var(--sky) 100%);
    border-top: 6px solid var(--sky);
  }
  .card-front .web {
    position: absolute; left: 38px; bottom: 26px;
    color: #fff; font-size: 18px; font-weight: 700; letter-spacing: 1px;
  }
</style>
</head>
<body>
  <section class="card card-back">
    <div class="brand">
      <span class="brand-dot"></span>
      <span class="brand-name">SkyvoraQ</span>
    </div>
    <p class="web">www.skyvoraq.com</p>
  </section>

  <section class="card card-front">
    <div class="band" role="img" aria-label="Decorative blue band along the bottom edge"></div>
    <div class="brand">
      <span class="brand-dot"></span>
      <span class="brand-name">SkyvoraQ</span>
    </div>
    <div class="divider"></div>
    <div class="contact">
      <h1 class="person">Dorian <span class="surname">Vellacott</span></h1>
      <p class="role">CEO / Founder</p>
      <p class="address">4827 Tollbeck Lane<br>Larkhaven, Calvera, 34951</p>
      <ul class="lines">
        <li><svg viewBox="0 0 16 16"><path d="M3 2l3 3-2 2c1 2 3 4 5 5l2-2 3 3-2 2C7 15 1 9 1 4z"/></svg>000.000.0000</li>
        <li><svg viewBox="0 0 16 16"><rect x="4" y="1" width="8" height="14" rx="1.5"/><path d="M7 12.5h2"/></svg>000.000.0000</li>
        <li><svg viewBox="0 0 16 16"><rect x="1" y="3" width="14" height="10"/><path d="M1 3l7 6 7-6"/></svg>dorian@skyvoraq.com</li>
      </ul>
    </div>
    <p class="web">www.skyvoraq.com</p>
  </section>
</body>
</html>
```